依頼概要
日本語学校のポスターデザインをお願いします。
今年の10月に新規開校します

サイズ:A0、A1、各1
学校情報:http://www.kesu.jp
ポスター使用目的:海外での学生募集説明会、海外教育機関への営業
納品形式:イラレ、jpeg、各1

ポスター内容:
・学校写真、学生寮写真(それぞれ枚数指定なし)
・「日本に留学しよう」のような誘い文句
・その他文章の作成をお願いします
・募集コース:4月期生、10月期生

要望:
・A1をメインで使用します。
・A0はA1を拡大したものでも結構ですし、別にデザインして頂いても結構です。
(報酬は変わらないので、ご了承下さい。すみません。)
・当方イラレを持っていないので、イラレの他に必ずjpeg形式またはofficeソフト形式で納品をお願いします。(photoshopは持ってます)
・シンプルというか、パッと見て分かり易い感じのデザインでお願いしたいですが、デザインの幅を狭めたくない気持ちもあります。
・学費含め費用関連は、載せないで下さい。
・入学案内関連の情報は、「募集コース」以外は載せないで下さい。

写真について:
・場所やアングルの指定などをして頂ければ、頑張って撮影してきます。
(もちろん、素人撮影です)
・10月に新規開校なので、授業風景の写真は用意できません。
・同じ理由で教員やスタッフ、人物の写真は用意ができません。
・花火大会のパーティーや、クリスマスパーティーの写真はあります。

日本語学校とは:(ご存知ない方もいらっしゃるかと思いますので、簡単に)
・生徒は全て外国籍の留学生です。
・日本の大学や大学院、専門学校への進学を目標に日本語学校で約2年、日本語の勉強をします。

当校の特徴:
・利根川の土手沿いに校舎があります。とっても静かです。
・校舎から約100mのところが花火大会の打ち上げ場所です。
・その他添付資料をご参照下さい。

その他:
ロゴのデータを添付しますのでご使用下さい。
学校に関連した文章も添付しておきますので、ご参考まで。
デザインの採用をさせて頂いた後で写真を撮ってきますので、その後に微調整をして納品をお願いします。
なので、納品まで少々時間がかかります。

以上、どうぞよろしくお願い致します。

生徒募集の為の宣伝ポスターを作る予定だったのですが、こちらのデザインは宣伝としての役割だけでなく、一つの絵として完成されていると思いました。空間を華やかに飾ってくれるデザインで、海外の教育機関だけでなく、商業施設にも持ち込み易いと思い、採用をさせて頂きました。

ご提案頂きましたワーカルの皆様。素敵なデザインをご提案頂き、ありがとうございました。期待以上の作品ばかりでスタッフ一同大変悩みました。今後もまたこちらに依頼をすることがあるかと思いますので、またご縁があればと思います。皆様のご発展をお祈り申し上げます。ありがとうございました。

```html
<!DOCTYPE html>
<html lang="ja">
<head>
<meta charset="utf-8">
<title>日本を学ぶ — STUDY JAPAN</title>
<link rel="stylesheet" href="https://fonts.googleapis.com/css2?family=Yuji+Syuku&family=Oswald:wght@500&family=Noto+Sans+JP:wght@400&family=Shippori+Mincho:wght@600&display=swap">
<style>
  :root {
    --paper: #ffffff;
    --ink: #1a1a1a;
    --orange: #e8692b;
    --sun-red: #d9291c;
    --blossom: #f3c6d0;
    --pagoda: #b8322a;
    --fuji-blue: #5b86c5;
    --pine: #4f6b3a;
    --brand-navy: #1f3f7a;
  }
  html, body { margin: 0; padding: 0; overflow: hidden; background: var(--paper); }
  .poster {
    position: relative;
    width: 849px;
    height: 1200px;
    overflow: hidden;
    background: var(--paper);
    color: var(--ink);
  }
  .hero-art {
    position: absolute;
    left: 0; top: 0;
    width: 849px; height: 660px;
  }
  .headline-learn, .headline-japan {
    position: absolute;
    margin: 0;
    font-family: "Yuji Syuku", serif;
    font-weight: 400;
    line-height: 1;
    color: var(--ink);
    writing-mode: vertical-rl;
  }
  .headline-learn {
    left: 28px; top: 14px;
    font-size: 112px;
    letter-spacing: 2px;
  }
  .headline-japan {
    left: 680px; top: 40px;
    font-size: 104px;
    letter-spacing: 2px;
  }
  .title-en {
    position: absolute;
    left: 0; right: 0; top: 650px;
    margin: 0;
    text-align: center;
    font-family: "Oswald", sans-serif;
    font-weight: 500;
    font-size: 98px;
    letter-spacing: 4px;
    line-height: 1;
    color: var(--orange);
  }
  .intro {
    position: absolute;
    left: 62px; right: 62px; top: 770px;
    margin: 0;
    font-family: "Noto Sans JP", sans-serif;
    font-size: 10.5px;
    line-height: 1.8;
    color: var(--orange);
  }
  .school-brand {
    position: absolute;
    left: 20px; top: 848px;
    width: 310px;
    text-align: center;
  }
  .brand-mark {
    width: 76px; height: 76px;
    margin: 0 auto 12px;
    background: var(--brand-navy);
  }
  .brand-ja {
    margin: 0 0 6px;
    font-family: "Shippori Mincho", serif;
    font-weight: 600;
    font-size: 24px;
    color: var(--brand-navy);
  }
  .brand-en {
    margin: 0;
    font-family: "Shippori Mincho", serif;
    font-weight: 600;
    font-size: 8px;
    letter-spacing: 0.5px;
    color: var(--brand-navy);
  }
  .campus-photo {
    position: absolute;
    left: 345px; top: 832px;
    width: 490px; height: 290px;
  }
</style>
</head>
<body>
<main class="poster">
  <svg class="hero-art" viewBox="0 0 849 660" role="img" aria-label="Illustration of Japan: a red rising sun with a torii gate, cherry blossom branches, a five-storey pagoda, Mount Fuji with waves, a pine tree with a crane and Tokyo Tower">
    <defs>
      <linearGradient id="japan-tones" x1="0" y1="0.5" x2="1" y2="0.5">
        <stop offset="0" stop-color="#e0402e"/>
        <stop offset="0.3" stop-color="#e86a5a"/>
        <stop offset="0.48" stop-color="#f3c6d0"/>
        <stop offset="0.7" stop-color="#f6dde3"/>
        <stop offset="0.85" stop-color="#8fb0db"/>
        <stop offset="1" stop-color="#5b86c5"/>
      </linearGradient>
    </defs>
    <path d="M60 360 C60 250 150 170 260 170 C330 170 380 120 450 100 C540 80 640 60 760 90 C800 200 820 330 800 420 C740 500 600 590 420 610 C280 625 140 600 90 520 C70 470 60 420 60 360 Z" fill="url(#japan-tones)" opacity="0.9"/>
  </svg>

  <h1 class="headline-learn">学ぶ</h1>
  <p class="headline-japan">日本を</p>

  <h2 class="title-en">STUDY JAPAN</h2>

  <p class="intro">北川リバーサイド国際学院は、静かな川沿いの校舎で日本語を学ぶ留学生のための学校です。日本の大学や大学院、専門学校への進学を目指し、約二年間で確かな日本語力を身につけます。校舎の近くでは毎年夏に花火大会が開かれ、季節の行事を通して日本の文化にも親しむことができます。募集コースは四月期生と十月期生です。私たちと一緒に日本で新しい一歩を踏み出しましょう。</p>

  <section class="school-brand">
    <div class="brand-mark"></div>
    <p class="brand-ja">北川リバーサイド国際学院</p>
    <p class="brand-en">KITAGAWA RIVERSIDE INTERNATIONAL ACADEMY</p>
  </section>

  <svg class="campus-photo" viewBox="0 0 490 290" role="img" aria-label="Photograph of the two-storey school building beside the riverbank, with trees and a blue sky">
    <defs>
      <linearGradient id="campus-tones" x1="0" y1="0" x2="0" y2="1">
        <stop offset="0" stop-color="#a9c4e0"/>
        <stop offset="0.45" stop-color="#7f93a8"/>
        <stop offset="1" stop-color="#6f8a4c"/>
      </linearGradient>
    </defs>
    <rect width="490" height="290" fill="url(#campus-tones)"/>
  </svg>
</main>
</body>
</html>
```